Industrial Professional Business Card Design (Vantrel Systems)

Would like professional looking business cards. Not too busy leaning towards minimal. Should have a slogan like:
"Industrial Automation and Control".

We are a tech company that programs industrial PLC computers. We also develop custom hardware solutions. Please use the logo for inspiration.

Target Market(s)

Mining, industrial, processing, automation, factory

Industry/Entity Type

Engineering

Contact Information for Business Card

Name, phone, email, website. job title.

Font styles to use
Other font styles liked:
• droid sans

Requirements
Must have
• Use colours that go well with the logo. Not too busy design.

```html
<!DOCTYPE html>
<html lang="en">
<head>
<meta charset="utf-8">
<title>Vantrel Systems – Business Card</title>
<link rel="stylesheet" href="https://fonts.googleapis.com/css2?family=Noto+Sans:wght@400;700&family=Sora:wght@300;400&display=swap">
<style>
  :root {
    --backdrop: #2a2a2a;
    --navy: #1f2d5c;
    --navy-deep: #1b2750;
    --teal: #2a7ea8;
    --orange: #f07a2a;
    --steel-blue: #2b5a86;
    --paper: #f7f7f5;
    --ink: #3a3a3a;
    --white: #ffffff;
  }
  * { box-sizing: border-box; margin: 0; padding: 0; }
  html, body {
    width: 1102px; height: 1200px; overflow: hidden;
    background: var(--backdrop);
  }
  .canvas { position: relative; width: 1102px; height: 1200px; }
  .card {
    position: absolute; left: 201px; width: 699px; height: 401px;
    border-radius: 26px; overflow: hidden;
  }
  .card--front { top: 179px; background: var(--navy); }
  .card--back { top: 624px; background: var(--paper); }

  .front__motif {
    position: absolute; right: 0; top: 0; width: 360px; height: 401px;
    background: radial-gradient(circle at 100% 70%, var(--teal) 0%, #245f8c 45%, rgba(31,45,92,0) 75%);
  }
  .front__brand {
    position: absolute; left: 46px; top: 280px;
    font-family: "Sora", sans-serif; font-weight: 300;
    font-size: 40px; color: var(--white); letter-spacing: -0.5px; white-space: nowrap;
  }
  .front__slogan {
    position: absolute; left: 46px; top: 348px;
    font-family: "Noto Sans", sans-serif; font-size: 18px; color: var(--white);
  }

  .back__brand {
    position: absolute; left: 20px; width: 300px; top: 236px;
    text-align: center;
    font-family: "Sora", sans-serif; font-weight: 400;
    font-size: 30px; color: var(--navy); letter-spacing: -0.5px; white-space: nowrap;
  }
  .back__divider {
    position: absolute; left: 347px; top: 137px; width: 2px; height: 142px;
    background: var(--orange);
  }
  .contact { position: absolute; left: 377px; top: 134px; font-family: "Noto Sans", sans-serif; }
  .contact__name { font-size: 24px; font-weight: 700; color: var(--steel-blue); letter-spacing: 0.2px; line-height: 28px; }
  .contact__title { font-size: 17px; color: var(--ink); line-height: 22px; }
  .contact__list { list-style: none; margin-top: 30px; }
  .contact__item { display: flex; align-items: center; gap: 7px; font-size: 17.5px; color: var(--ink); line-height: 24px; }
  .contact__icon { width: 15px; height: 15px; flex: none; }
</style>
</head>
<body>
<main class="canvas">
  <section class="card card--front">
    <div class="front__motif" role="img" aria-label="Large decorative brand motif area in teal and navy"></div>
    <div class="front__brand">Vantrel Systems</div>
    <div class="front__slogan">Industrial Automation and Control</div>
  </section>

  <section class="card card--back">
    <div class="back__brand">Vantrel Systems</div>
    <div class="back__divider"></div>
    <div class="contact">
      <div class="contact__name">DANIEL REYES</div>
      <div class="contact__title">President</div>
      <ul class="contact__list">
        <li class="contact__item">
          <svg class="contact__icon" viewBox="0 0 16 16" aria-hidden="true"><path fill="#f07a2a" d="M3.5 1.5l2.3 2.6-1.2 1.6c.9 1.9 2.4 3.4 4.3 4.3l1.6-1.2 2.6 2.3-1.4 2.2C6.5 13.4 2.6 9.5 1.4 3.3z"/></svg>
          555-014-2870
        </li>
        <li class="contact__item">
          <svg class="contact__icon" viewBox="0 0 16 16" aria-hidden="true"><rect x="1" y="3.5" width="14" height="9" fill="#f07a2a"/><path d="M1.5 4l6.5 5 6.5-5" stroke="#fff" stroke-width="1.3" fill="none"/></svg>
          info@vantrelsystems.com
        </li>
        <li class="contact__item">
          <svg class="contact__icon" viewBox="0 0 16 16" aria-hidden="true"><circle cx="8" cy="8" r="7" fill="#f07a2a"/><path d="M1 8h14M8 1c-3 3.5-3 10.5 0 14M8 1c3 3.5 3 10.5 0 14" stroke="#fff" stroke-width="1" fill="none"/></svg>
          www.vantrelsystems.com
        </li>
      </ul>
    </div>
  </section>
</main>
</body>
</html>
```